Brochure- single fold

We need a design for nursing mothers who are having problems with their milk supply. we provide a medication that can help increase the supply for the nursing mother.

______ content below_____________
HELP! My Mommy Needs Milk!

Read more to discover how compounded Veralin could help you produce more milk for your baby:

We all know that breast milk is the best for baby! Additionally, one of the best-kept secrets about breastfeeding is that it's as healthy for mothers as for babies. Not only does lactation continue the natural physiologic process begun with conception and pregnancy, but it provides many short and long-term health benefits. According to Varden Public Wellness Bureau, the benefits of breastfeeding included fewer episodes of acute respiratory illnesses, inner-ear infections and gastroenteritis in babies.

A number of studies have shown other potential health advantages that mothers can enjoy through breastfeeding. These include optimal metabolic profiles, reduced risk of various cancers, and psychological benefits.

What is Veralin?

Veralin is a compounded medication that is prescribed by physicians because there are several studies to show that it works to increase milk production and that it is safe for both mother and baby.

Veralin Compared to Metoclopramide (Dostrem™)

Veralin is similar to metoclopramide (Dostrem™), which is also known to increase milk production. With metoclopramide, however, many mothers are not able to tolerate the side effects such as fatigue, irritability, and depression caused by its use. Veralin is an excellent alternative for this reason, but also because some studies show extremely limited amounts of Veralin passing through the blood-brain barrier and into breast milk.

How Can I get Veralin?

Veralin is a compounded medication only available by prescription from your physician. You may request a prescription form by visiting www.plentifulfeedhelp.example, by emailing info@plentifulfeedhelp.example, or by contacting (555) 718-2043.

Veralin by Brackenford Pharmaceuticals, Inc.
2750 Quimby Ave #300 Los Angeles, CA 90025
Ph: (555) 718-2043 Fax: (555) 718-2044

Target Market(s)

mothers with infants to 2 years old.

Industry/Entity Type

Health

Requirements
Must have
• single fold design- back side of page is our contact info and a space to mail the brochure.

```html
<!DOCTYPE html>
<html lang="en">
<head>
<meta charset="utf-8">
<title>Veralin Single-Fold Brochure</title>
<link rel="stylesheet" href="https://fonts.googleapis.com/css2?family=PT+Sans:wght@400;700&display=swap">
<style>
  :root {
    --stage: #2b2b2d;
    --stage-light: #3a3a3d;
    --plum-deep: #4a1d4c;
    --plum: #6b2a68;
    --magenta: #9c3f86;
    --magenta-light: #b35a9b;
    --gold: #f2bf2f;
    --text-light: #f6e4f1;
    --mail-line: rgba(246, 228, 241, 0.45);
    --photo-warm: #c99486;
    --photo-dark: #3b2a30;
    --photo-cool: #a9b8c8;
  }
  * { box-sizing: border-box; margin: 0; padding: 0; }
  html, body { width: 818px; height: 1200px; overflow: hidden; }
  body {
    background: radial-gradient(ellipse at 50% 45%, var(--stage-light), var(--stage) 70%);
    font-family: "PT Sans", Arial, sans-serif;
    position: relative;
    color: var(--text-light);
  }
  .sheet {
    position: absolute;
    left: 0;
    width: 818px; height: 546px;
    overflow: hidden;
    background: var(--magenta);
  }
  .sheet--inside { top: 34px; }
  .sheet--outside { top: 620px; display: flex; }

  .photo {
    position: absolute;
    background:
      radial-gradient(ellipse at 62% 45%, var(--photo-warm) 0%, #a86e6a 35%, transparent 62%),
      linear-gradient(100deg, var(--photo-cool) 0%, #d9dde2 22%, var(--photo-dark) 48%, #5b3a3e 100%);
  }
  .sheet--inside .photo { left: 0; top: 0; width: 818px; height: 360px; }
  .curves { position: absolute; left: 0; top: 0; }

  .inside-content {
    position: absolute; left: 0; right: 0; top: 372px;
    display: grid; grid-template-columns: 1fr 1fr; column-gap: 40px;
    padding: 0 32px;
    font-size: 10px; line-height: 1.42;
  }
  .section-title {
    color: var(--gold);
    font-weight: 700;
    font-size: 11px;
    margin-bottom: 3px;
  }
  .section-body { margin-bottom: 10px; }
  .contact-link { color: var(--gold); }

  /* Outside: back panel + front cover */
  .panel { position: relative; width: 409px; height: 546px; }
  .panel--back {
    background: linear-gradient(180deg, var(--plum) 0%, var(--plum-deep) 100%);
    padding: 36px 32px;
    border-right: 1px solid rgba(0, 0, 0, 0.25);
  }
  .back-contact { font-size: 11px; line-height: 1.5; }
  .back-contact .brand-name {
    color: var(--gold);
    font-weight: 700;
    font-size: 15px;
    margin-bottom: 4px;
  }
  .mail-area {
    position: absolute;
    left: 32px; right: 32px; bottom: 36px;
    height: 230px;
    border: 1px solid var(--mail-line);
    padding: 16px;
  }
  .mail-return { font-size: 9px; line-height: 1.4; }
  .mail-stamp {
    position: absolute; top: 16px; right: 16px;
    width: 52px; height: 60px;
    border: 1px dashed var(--mail-line);
  }
  .mail-lines { position: absolute; left: 130px; right: 30px; bottom: 40px; }
  .mail-lines span {
    display: block; height: 1px; background: var(--mail-line);
    margin-top: 26px;
  }

  .panel--cover { background: linear-gradient(180deg, var(--magenta-light), var(--magenta)); }
  .panel--cover .photo { left: 0; top: 0; width: 409px; height: 200px; }
  .cover-content {
    position: absolute; left: 28px; right: 28px; top: 196px;
    font-size: 9.6px; line-height: 1.42;
  }
  .cover-headline {
    color: var(--gold);
    font-weight: 700;
    font-size: 25px;
    line-height: 1.1;
    margin-bottom: 6px;
  }
  .cover-lead {
    font-weight: 700;
    font-size: 11px;
    margin-bottom: 8px;
  }
  .cover-content p + p { margin-top: 7px; }
</style>
</head>
<body>
  <section class="sheet sheet--inside" aria-label="Brochure inside spread">
    <div class="photo" role="img" aria-label="Photograph of a baby drinking from a bottle"></div>
    <svg class="curves" width="818" height="546" viewBox="0 0 818 546" aria-hidden="true">
      <defs>
        <linearGradient id="insideGrad" x1="0" y1="0" x2="0" y2="1">
          <stop offset="0" stop-color="#b35a9b"/>
          <stop offset="1" stop-color="#9c3f86"/>
        </linearGradient>
      </defs>
      <path d="M0 170 C 180 300 520 330 818 250 L818 546 L0 546 Z" fill="#4a1d4c"/>
      <path d="M0 205 C 200 320 540 335 818 270" fill="none" stroke="#f2bf2f" stroke-width="5"/>
      <path d="M0 225 C 220 335 560 345 818 285 L818 546 L0 546 Z" fill="#6b2a68"/>
      <path d="M0 285 C 250 360 580 350 818 300 L818 546 L0 546 Z" fill="url(#insideGrad)"/>
    </svg>

    <div class="inside-content">
      <div class="column">
        <h2 class="section-title">What is Veralin?</h2>
        <p class="section-body">Veralin is a compounded medication that is prescribed by physicians because there are several studies to show that it works to increase milk production and that it is safe for both mother and baby.</p>
        <h2 class="section-title">Veralin Compared to Metoclopramide (Dostrem™)</h2>
        <p class="section-body">Veralin is similar to metoclopramide (Dostrem™), which is also known to increase milk production. With metoclopramide, however, many mothers are not able to tolerate the side effects such as fatigue, irritability, and depression caused by its use.</p>
      </div>
      <div class="column">
        <p class="section-body">Veralin is an excellent alternative for this reason, but also because some studies show extremely limited amounts of Veralin passing through the blood-brain barrier and into breast milk.</p>
        <h2 class="section-title">How Can I get Veralin?</h2>
        <p class="section-body">Veralin is a compounded medication only available by prescription from your physician. You may request a prescription form by visiting <span class="contact-link">www.plentifulfeedhelp.example</span>, by emailing <span class="contact-link">info@plentifulfeedhelp.example</span>, or by contacting (555) 718-2043.</p>
      </div>
    </div>
  </section>

  <section class="sheet sheet--outside" aria-label="Brochure outside: back panel and front cover">
    <div class="panel panel--back">
      <div class="back-contact">
        <p class="brand-name">Veralin</p>
        <p>by Brackenford Pharmaceuticals, Inc.</p>
        <p>2750 Quimby Ave #300 Los Angeles, CA 90025</p>
        <p>Ph: (555) 718-2043 &nbsp;Fax: (555) 718-2044</p>
        <p class="contact-link">www.plentifulfeedhelp.example</p>
        <p class="contact-link">info@plentifulfeedhelp.example</p>
      </div>
      <div class="mail-area" aria-label="Mailing area">
        <div class="mail-return">
          <p>Brackenford Pharmaceuticals, Inc.</p>
          <p>2750 Quimby Ave #300</p>
          <p>Los Angeles, CA 90025</p>
        </div>
        <div class="mail-stamp"></div>
        <div class="mail-lines"><span></span><span></span><span></span></div>
      </div>
    </div>

    <div class="panel panel--cover">
      <div class="photo" role="img" aria-label="Photograph of a baby drinking from a bottle"></div>
      <svg class="curves" width="409" height="546" viewBox="0 0 409 546" aria-hidden="true">
        <path d="M0 120 C 120 185 280 195 409 150 L409 546 L0 546 Z" fill="#4a1d4c"/>
        <path d="M0 138 C 120 196 280 204 409 162" fill="none" stroke="#f2bf2f" stroke-width="4"/>
        <path d="M0 150 C 130 204 290 208 409 172 L409 546 L0 546 Z" fill="#6b2a68"/>
        <path d="M0 175 C 140 215 300 212 409 185 L409 546 L0 546 Z" fill="#b35a9b"/>
      </svg>
      <div class="cover-content">
        <h1 class="cover-headline">HELP! My Mommy Needs Milk!</h1>
        <p class="cover-lead">Read more to discover how compounded Veralin could help you produce more milk for your baby:</p>
        <p>We all know that breast milk is the best for baby! Additionally, one of the best-kept secrets about breastfeeding is that it's as healthy for mothers as for babies. Not only does lactation continue the natural physiologic process begun with conception and pregnancy, but it provides many short and long-term health benefits. According to Varden Public Wellness Bureau, the benefits of breastfeeding included fewer episodes of acute respiratory illnesses, inner-ear infections and gastroenteritis in babies.</p>
        <p>A number of studies have shown other potential health advantages that mothers can enjoy through breastfeeding. These include optimal metabolic profiles, reduced risk of various cancers, and psychological benefits.</p>
      </div>
    </div>
  </section>
</body>
</html>
```